Kickbut Home Page Design built to Sell

We need a new home page layout. The website is working now but we need a refresh. Our business has slowed down since a few years ago. We need to show we build ecommerce and membership websites. Here is the page now: https://www.pelvrakwerks.graphics/new-home/

Target Market(s)

Women, solopreneurs, artists, politicians

Industry/Entity Type

Design Agency

Number of Pages Required

1 page

Font styles to use
Sans Serif

Colors
b8a6cd
fabb94
acd136
00a990

Requirements
Must have
• Video header
Section for text and Step process similar to this website: https://quillbarrowstudio.com/ [This is out sister company]
Places for images.
Call to action lead gen form and Get a quote.
The menu should show WEB, PRINT, VIDEO
Nice to have
• I LOVE this company: https://tavelmorn.com/guide/
Area for testimonials
Should not have
• We don't want a duplicate of https://quillbarrowstudio.com/

```html
<!DOCTYPE html>
<html lang="en">
<head>
<meta charset="utf-8">
<title>Pelvrakwerks — Web Design Agency</title>
<link href="https://fonts.googleapis.com/css2?family=Montserrat:wght@600;700;800&family=Open+Sans:wght@400;600;700&display=swap" rel="stylesheet">
<style>
:root{
  --green:#00a990;
  --green-dark:#008a75;
  --lime:#acd136;
  --ink:#222222;
  --body:#555555;
  --light:#f2f2f2;
  --white:#ffffff;
  --lavender:#b8a6cd;
  --peach:#fabb94;
}
*{margin:0;padding:0;box-sizing:border-box}
html,body{width:1200px;height:4528px;overflow:hidden}
body{font-family:"Open Sans",Arial,sans-serif;color:var(--body);background:var(--white);position:relative}
h1,h2,h3,h4{font-family:"Montserrat",Arial,sans-serif;color:var(--ink)}
.btn{display:inline-block;background:var(--lime);color:var(--white);font-family:"Montserrat",Arial,sans-serif;font-weight:700;font-size:14px;letter-spacing:.5px;padding:14px 30px;border-radius:30px;text-transform:uppercase}
.section-title{text-align:center;font-size:34px;font-weight:800;text-transform:uppercase}
.title-rule{width:70px;height:4px;background:var(--lime);margin:18px auto 0}

/* hero */
.hero{position:absolute;left:0;top:0;width:1200px;height:620px;background:linear-gradient(180deg,#2f4a4a 0%,#3c5d5c 45%,#2a3b3e 100%)}
.nav{position:absolute;left:100px;right:100px;top:26px;height:50px;display:flex;align-items:center}
.brand{font-family:"Montserrat",Arial,sans-serif;font-weight:800;font-size:30px;color:var(--white);letter-spacing:1px}
.brand-tag{display:block;font-size:9px;letter-spacing:2px;font-weight:600;color:var(--white);margin-top:2px}
.menu{margin-left:auto;display:flex;gap:60px;align-items:center;font-family:"Montserrat",Arial,sans-serif;font-weight:700;color:var(--white);font-size:15px}
.menu .btn{padding:12px 26px;font-size:13px}
.hero-copy{position:absolute;left:0;right:0;top:228px;text-align:center;color:var(--white)}
.hero-copy h1{color:var(--white);font-size:44px;font-weight:800;line-height:1.2;text-transform:uppercase}
.hero-copy p{font-family:"Montserrat",Arial,sans-serif;font-weight:700;font-size:16px;margin:18px 0 26px;text-transform:uppercase}

/* services */
.services{position:absolute;left:0;top:620px;width:1200px;height:540px;background:var(--white)}
.arrow{position:absolute;top:128px;width:38px;height:38px;border-radius:50%;background:var(--white);box-shadow:0 2px 6px rgba(0,0,0,.25);display:flex;align-items:center;justify-content:center}
.service-card{position:absolute;top:80px;width:312px;text-align:center}
.service-card .photo{height:208px;border-radius:8px 8px 0 0}
.service-card h3{font-size:18px;font-weight:700;margin:24px 0 14px;text-transform:uppercase}
.service-card p{font-size:15px;line-height:1.6;padding:0 18px}

/* agency */
.agency{position:absolute;left:0;top:1190px;width:1200px;height:640px;background:var(--green)}
.agency-copy{position:absolute;left:100px;top:110px;width:470px;color:var(--white)}
.agency-copy h2{color:var(--white);font-size:34px;font-weight:800;line-height:1.15;text-transform:uppercase}
.agency-copy p{font-size:14px;line-height:1.7;margin:22px 0}
.agency-copy .lead{font-family:"Montserrat",Arial,sans-serif;font-weight:700;font-size:14px;text-transform:uppercase;margin:0 0 26px}
.agency-photo{position:absolute;left:620px;top:0;width:580px;height:640px;border-radius:320px 0 0 320px / 640px 0 0 640px;background:linear-gradient(135deg,#cfd8dc,#8fa5ad 60%,#5e7a82)}

/* process */
.process{position:absolute;left:0;top:1830px;width:1200px;height:530px;background:var(--light)}
.process .section-title{margin-top:84px}
.step{position:absolute;top:240px;width:300px;text-align:center}
.step svg{display:block;margin:0 auto}
.step h3{color:var(--green);font-size:18px;font-weight:700;margin:20px 0 12px;text-transform:uppercase}
.step p{font-size:15px;line-height:1.6}

/* work */
.work{position:absolute;left:0;top:2360px;width:1200px;height:620px;background:var(--white)}
.work .section-title{margin-top:90px}
.work-grid{position:absolute;left:108px;top:168px;display:grid;grid-template-columns:repeat(4,232px);grid-template-rows:172px 180px;gap:16px 20px}
.work-grid div{border-radius:2px}

/* testimonials */
.testimonials{position:absolute;left:0;top:2980px;width:1200px;height:560px;background:#f5f5f5}
.testimonials .section-title{margin-top:108px;font-size:32px}
.quote-mark{position:absolute;left:188px;top:196px;font-family:Georgia,serif;font-size:120px;line-height:1;color:#c9c9c9}
.client-photo{position:absolute;left:238px;top:180px;width:200px;height:200px;border-radius:50%;background:linear-gradient(160deg,#dfe3e6,#8d9aa3)}
.testimonial-text{position:absolute;left:600px;top:190px;width:500px;font-size:14px;line-height:1.7}
.client-name{position:absolute;left:600px;top:400px;font-family:"Montserrat",Arial,sans-serif;font-weight:700;font-size:18px;color:var(--green);text-transform:uppercase}
.client-role{position:absolute;left:600px;top:426px;font-size:12px;color:var(--lime);text-transform:uppercase}
.slider-nav{position:absolute;left:1012px;top:400px;display:flex;gap:8px}
.slider-nav span{width:40px;height:28px;display:flex;align-items:center;justify-content:center}
.slider-nav .active{background:var(--white);box-shadow:0 1px 4px rgba(0,0,0,.2)}

/* quote form */
.quote{position:absolute;left:0;top:3540px;width:1200px;height:620px;background:linear-gradient(180deg,#0aa78f,#00997f)}
.quote h2{position:absolute;left:0;right:0;top:100px;text-align:center;color:var(--white);font-size:34px;font-weight:800;text-transform:uppercase}
.quote .title-rule{position:absolute;left:565px;top:152px;margin:0}
.contact-row{position:absolute;left:0;right:0;top:176px;display:flex;justify-content:center;gap:36px;color:var(--white);font-size:15px}
.contact-row span{display:flex;align-items:center;gap:8px}
.quote-art{position:absolute;left:260px;top:262px;width:320px;height:320px;border-radius:6px;background:linear-gradient(160deg,rgba(255,255,255,.25),rgba(255,255,255,.08))}
.quote-form{position:absolute;left:652px;top:232px;width:328px}
.field{height:34px;background:var(--white);border-radius:17px;margin-bottom:12px;padding:0 16px;font-size:12px;color:#888;display:flex;align-items:center}
.field.message{height:100px;border-radius:14px;align-items:flex-start;padding-top:10px}
.quote-form .btn{display:block;text-align:center;margin-top:6px;padding:10px 0}

/* footer */
.footer{position:absolute;left:0;top:4160px;width:1200px;height:368px;background:var(--white)}
.footer .brand{position:absolute;left:100px;top:140px;color:var(--ink);font-size:36px}
.footer .brand-tag{color:var(--ink)}
.footer-col{position:absolute;top:44px}
.footer-col h4{font-size:16px;font-weight:800;text-transform:uppercase;margin-bottom:16px}
.footer-col ul{list-style:none;display:grid;grid-template-columns:auto auto;column-gap:60px;row-gap:12px;font-size:14px;color:var(--body)}
.footer-col.single ul{grid-template-columns:auto}
.social{display:flex;gap:10px}
.social span{width:20px;height:20px;border-radius:50%;background:var(--ink)}
.partner{display:flex;align-items:center;gap:10px;margin-top:16px;font-family:"Open Sans",Arial,sans-serif;font-weight:700;font-size:14px;color:var(--ink)}
.partner span{width:30px;height:30px;border-radius:50%;background:var(--lime)}
.footer-bar{position:absolute;left:0;right:0;bottom:0;height:52px;border-top:1px solid #ddd;display:flex;align-items:center;justify-content:center;font-size:13px}
.footer-bar em{position:absolute;right:30px;font-style:normal;font-size:11px}
</style>
</head>
<body>

<header class="hero" role="img" aria-label="Video header: team working at desks with laptops, dimmed teal overlay">
  <nav class="nav">
    <div class="brand">PELVRAKWERKS<span class="brand-tag">GRAPHICS AND WEB DESIGN STUDIO</span></div>
    <div class="menu"><span>WEB</span><span>PRINT</span><span>VIDEO</span><span class="btn">Get a Quote</span></div>
  </nav>
  <div class="hero-copy">
    <h1>Lead generating websites that move<br>your business forward</h1>
    <p>Your company deserves a website that can inspire people to take action</p>
    <span class="btn">Watch Video</span>
  </div>
</header>

<section class="services">
  <span class="arrow" style="left:84px"><svg width="14" height="14" viewBox="0 0 14 14"><path d="M9 2 4 7l5 5" fill="none" stroke="#333" stroke-width="2"/></svg></span>
  <span class="arrow" style="left:1078px"><svg width="14" height="14" viewBox="0 0 14 14"><path d="M5 2l5 5-5 5" fill="none" stroke="#333" stroke-width="2"/></svg></span>
  <article class="service-card" style="left:108px">
    <div class="photo" role="img" aria-label="Photo: laptop with settings icons for website maintenance" style="background:linear-gradient(135deg,#d9dde0,#6f7d86)"></div>
    <h3>Website Maintenance</h3>
    <p>Want to keep your business growing? Your website is crucial to your growth and success. When operating seamlessly with your goals.</p>
  </article>
  <article class="service-card" style="left:444px">
    <div class="photo" role="img" aria-label="Photo: artist portfolio website on a desktop screen" style="background:linear-gradient(135deg,#e7e3ea,#b8a6cd)"></div>
    <h3>Artist Website</h3>
    <p>When you are in the art world you need to show your craft to get exposure, gigs and sales. We love working with artists that value good design!</p>
  </article>
  <article class="service-card" style="left:780px">
    <div class="photo" role="img" aria-label="Photo: logo sketches and stationery on a desk" style="background:linear-gradient(135deg,#f2ece6,#c8b8a6)"></div>
    <h3>Logo Design</h3>
    <p>We create logos for all kinds of companies and brands. A logo can be a namehead or a monogram, emblem, symbol or sign. A logo can take a week or a year to develop.</p>
  </article>
</section>

<section class="agency">
  <div class="agency-copy">
    <h2>We are a web design<br>agency</h2>
    <p>We help brands win online with beautifully designed websites and effective digital marketing strategies that deliver results to help your business grow. Pelvrakwerks is a New England web design agency providing high quality, professional and reliable websites, web page design and graphic design services to individuals, nonprofits, small, medium sized businesses, and political campaigns. We are a small team of highly professional web consultants with over 20 years of knowledge and experience and we'd love to help you win!</p>
    <p class="lead">Design is the silent ambassador of your brand</p>
    <span class="btn">Get in Touch</span>
  </div>
  <div class="agency-photo" role="img" aria-label="Photo: designers collaborating in a bright office"></div>
</section>

<section class="process">
  <h2 class="section-title">The process is simple</h2>
  <div class="title-rule"></div>
  <div class="step" style="left:150px">
    <svg width="64" height="64" viewBox="0 0 64 64" fill="none" stroke="#00a990" stroke-width="2.5"><rect x="12" y="8" width="36" height="48" rx="2"/><path d="M20 22h20M20 32h20M20 42h12"/><path d="M52 14l-14 30-4 6 1-7 14-30z"/></svg>
    <h3>Tell us your needs</h3>
    <p>Fill out our easy questionnaire so we can understand your problems.</p>
  </div>
  <div class="step" style="left:450px">
    <svg width="64" height="64" viewBox="0 0 64 64" fill="none" stroke="#00a990" stroke-width="2.5"><path d="M16 10l8 10-5 5c3 7 9 13 16 16l5-5 10 8-6 8C28 50 14 36 8 18z"/><path d="M38 14a14 14 0 0 1 12 12M38 6a22 22 0 0 1 20 20"/></svg>
    <h3>Phone Call</h3>
    <p>Book a time to have a chat in case we have more question about your goals.</p>
  </div>
  <div class="step" style="left:750px">
    <svg width="64" height="64" viewBox="0 0 64 64" fill="none" stroke="#00a990" stroke-width="2.5"><rect x="8" y="18" width="48" height="36" rx="3"/><path d="M24 18v-6h16v6M8 32h48M30 32v6h4v-6"/></svg>
    <h3>Custom quote arrives</h3>
    <p>Once we have made your plan, you'll get to work to build and launch your new website.</p>
  </div>
</section>

<section class="work">
  <h2 class="section-title">Examples of our work</h2>
  <div class="title-rule"></div>
  <div class="work-grid">
    <div role="img" aria-label="Portfolio: wireframe sketches" style="background:linear-gradient(135deg,#e9eef2,#9fb2c0)"></div>
    <div role="img" aria-label="Portfolio: website on a desktop monitor" style="background:linear-gradient(135deg,#dfe3e7,#7f8c96)"></div>
    <div role="img" aria-label="Portfolio: laptop with site design" style="background:linear-gradient(135deg,#e3e0e8,#8a8597)"></div>
    <div role="img" aria-label="Portfolio: responsive site on devices" style="background:linear-gradient(135deg,#cfd6db,#56646d)"></div>
    <div role="img" aria-label="Portfolio: colourful web design mockup" style="background:linear-gradient(135deg,#bfe3f0,#2b86b8)"></div>
    <div role="img" aria-label="Portfolio: designer drawing layouts" style="background:linear-gradient(135deg,#ecebe6,#a7a496)"></div>
    <div role="img" aria-label="Portfolio: site shown on screen and tablet" style="background:linear-gradient(135deg,#eef0f1,#9aa3a8)"></div>
    <div role="img" aria-label="Portfolio: mobile and laptop screens" style="background:linear-gradient(135deg,#d6dbd9,#5d6b66)"></div>
  </div>
</section>

<section class="testimonials">
  <h2 class="section-title">Why our clients love us</h2>
  <div class="title-rule"></div>
  <div class="quote-mark">“</div>
  <div class="client-photo" role="img" aria-label="Client portrait photo"></div>
  <p class="testimonial-text">Dana Baker was great to work with and extremely knowledgeable and accessible. I especially appreciated his well thought out design process and the client videos he created to walk me through various stages of it. I received lots of great feedback on the visual look, user friendliness, and rich content of my website throughout the campaign and was so excited overall. I highly recommend Dana and Quillbarrow Studio for your next project!</p>
  <div class="client-name">Dorian Velasko</div>
  <div class="client-role">Founder, Velasko Campaigns</div>
  <div class="slider-nav">
    <span class="active"><svg width="16" height="10" viewBox="0 0 16 10"><path d="M15 5H2M6 1 2 5l4 4" fill="none" stroke="#333" stroke-width="1.6"/></svg></span>
    <span><svg width="16" height="10" viewBox="0 0 16 10"><path d="M1 5h13M10 1l4 4-4 4" fill="none" stroke="#333" stroke-width="1.6"/></svg></span>
  </div>
</section>

<section class="quote">
  <h2>Get in quote</h2>
  <div class="title-rule"></div>
  <div class="contact-row">
    <span><svg width="14" height="14" viewBox="0 0 14 14"><path d="M3 1l2 3-1.5 1.5a8 8 0 0 0 5 5L10 9l3 2-1 2.5C6 13 1 8 .5 2z" fill="#acd136"/></svg>1-555-014-2280</span>
    <span><svg width="12" height="16" viewBox="0 0 12 16"><path d="M6 0a6 6 0 0 1 6 6c0 4-6 10-6 10S0 10 0 6a6 6 0 0 1 6-6z" fill="#acd136"/><circle cx="6" cy="6" r="2" fill="#00a990"/></svg>27 Larkspur Ave, Fenwick MA 01999</span>
  </div>
  <div class="quote-art" role="img" aria-label="Illustration: envelope with a checked document"></div>
  <form class="quote-form">
    <div class="field">First Name</div>
    <div class="field">Last Name</div>
    <div class="field">Phone</div>
    <div class="field">Email Address</div>
    <div class="field message">Message</div>
    <span class="btn">Submit</span>
  </form>
</section>

<footer class="footer">
  <div class="brand">PELVRAKWERKS<span class="brand-tag">GRAPHICS AND WEB DESIGN STUDIO</span></div>
  <div class="footer-col" style="left:472px">
    <h4>Useful Links</h4>
    <ul><li>Web</li><li>How it works</li><li>Print</li><li>News</li><li>Video</li><li>Contact</li></ul>
  </div>
  <div class="footer-col single" style="left:752px">
    <h4>Fast To</h4>
    <ul><li>Terms and Use</li><li>Privacy Policy</li><li>Sitemap</li></ul>
  </div>
  <div class="footer-col" style="left:928px">
    <h4>Follow Us</h4>
    <div class="social"><span></span><span></span><span></span><span></span><span></span></div>
    <div class="partner"><span></span>Quillbarrow Studio</div>
  </div>
  <div class="footer-bar">© 2021 Pelvrakwerks Graphics. All rights reserved<em>1 of 4</em></div>
</footer>

</body>
</html>
```